Verostel business card

Business card for sustainable investment company called "Verostel". Verostel is an exchange platform selling carbon credits between buyers and sellers. Carbon Credits are an environmental commodity for reducing global carbon emissions.

the card should obviously have our logo and the theme should be sustainability/environment mixed with a trading platform.

Contact Information for Business Card

Logo, Name, Title, Phone, Email

Colors
0054AA
0677BA
7BADD7
CADEEF
E8F1F8
0094D4
00A9DD
6FCCEA
C7EBF8
E9F6FB
00AB8E
00BBA5
67D7C9
C6EFE9
E9F9F6
59FF00
82FF00
B8FF75
E3FFCB
F4FFEA

```html
<!DOCTYPE html>
<html lang="en">
<head>
<meta charset="UTF-8">
<title>Verostel Business Card</title>
<link href="https://fonts.googleapis.com/css2?family=Montserrat:wght@400;500;700;800&display=swap" rel="stylesheet">
<style>
  :root {
    --navy: #152a57;
    --sky: #5aaad6;
    --white: #ffffff;
    --backdrop: #2b2c2e;
  }
  * { margin: 0; padding: 0; box-sizing: border-box; }
  html, body {
    width: 1200px; height: 960px; overflow: hidden;
    background: var(--backdrop);
    font-family: "Montserrat", sans-serif;
  }
  .canvas { position: relative; width: 1200px; height: 960px; }
  .card {
    position: absolute; left: 250px;
    width: 700px; height: 400px;
    border-radius: 22px; overflow: hidden;
  }
  .card--front { top: 60px; background: var(--navy); }
  .card--back { top: 500px; background: var(--white); }

  .brand {
    position: absolute; display: flex; align-items: center; gap: 16px;
    font-weight: 800; letter-spacing: 1px; text-transform: uppercase;
  }
  .brand__dot { border-radius: 50%; background: var(--sky); }
  .card--front .brand {
    left: 50%; top: 50%; transform: translate(-50%, -50%);
    font-size: 58px; color: var(--white);
  }
  .card--front .brand__dot { width: 42px; height: 42px; }
  .card--back .brand {
    right: 70px; top: 62px; font-size: 40px; color: var(--navy);
  }
  .card--back .brand__dot { width: 30px; height: 30px; }

  .wave { position: absolute; inset: 0; }

  .identity__bar {
    position: absolute; left: 0; top: 150px; width: 10px; height: 62px;
    background: var(--navy);
  }
  .identity { position: absolute; left: 50px; top: 150px; color: var(--navy); }
  .identity__name { font-size: 30px; font-weight: 800; letter-spacing: 1.5px; line-height: 1.1; }
  .identity__title { font-size: 17px; font-weight: 500; letter-spacing: 1.5px; margin-top: 2px; }

  .contact {
    position: absolute; left: 330px; top: 280px;
    color: var(--white); font-size: 14px; font-weight: 500; line-height: 1.3;
    list-style: none;
  }
  .contact__address { margin-bottom: 8px; }
  .contact__item { display: flex; align-items: center; gap: 10px; margin-top: 4px; }
  .contact__icon { width: 15px; height: 15px; flex: none; }
</style>
</head>
<body>
<main class="canvas">

  <section class="card card--front" aria-label="Card front">
    <div class="brand"><span class="brand__dot"></span>Verostel</div>
  </section>

  <section class="card card--back" aria-label="Card back">
    <svg class="wave" viewBox="0 0 700 400" width="700" height="400" aria-hidden="true">
      <path d="M240,268 C380,222 560,205 635,178 C685,155 700,110 700,70 L700,100 C690,160 620,228 480,245 C380,256 300,262 240,268 Z" fill="var(--sky)"/>
      <path d="M190,400 C210,320 250,282 340,266 C470,245 630,236 675,160 C690,135 698,115 700,108 L712,108 L712,412 L180,412 Z" fill="var(--navy)" stroke="var(--white)" stroke-width="6"/>
    </svg>

    <div class="brand"><span class="brand__dot"></span>Verostel</div>

    <span class="identity__bar"></span>
    <div class="identity">
      <div class="identity__name">DORIAN VALE</div>
      <div class="identity__title">MANAGER</div>
    </div>

    <ul class="contact">
      <li class="contact__address">2716 Alder Crest Rd. Meadow Lane<br>Ave Brookfield, MN 04512</li>
      <li class="contact__item">
        <svg class="contact__icon" viewBox="0 0 16 16" aria-hidden="true"><path d="M3 1.5l3 .5 1 3-1.8 1.3a8 8 0 0 0 4.5 4.5L11 9l3 1 .5 3-2 1.5C6.5 14 2 9.5 1.5 3.5z" fill="var(--sky)"/></svg>
        555-204-3318
      </li>
      <li class="contact__item">
        <svg class="contact__icon" viewBox="0 0 16 16" aria-hidden="true"><rect x="1" y="3" width="14" height="10" rx="1" fill="var(--sky)"/><path d="M1.5 3.5L8 9l6.5-5.5" fill="none" stroke="var(--navy)" stroke-width="1.4"/></svg>
        hello@verostelmail.com
      </li>
      <li class="contact__item">
        <svg class="contact__icon" viewBox="0 0 16 16" aria-hidden="true"><circle cx="8" cy="8" r="6.5" fill="none" stroke="var(--sky)" stroke-width="1.5"/><ellipse cx="8" cy="8" rx="2.8" ry="6.5" fill="none" stroke="var(--sky)" stroke-width="1.2"/><path d="M1.5 8h13M2.5 5h11M2.5 11h11" stroke="var(--sky)" stroke-width="1.1"/></svg>
        www.verostelexchange.com
      </li>
    </ul>
  </section>

</main>
</body>
</html>
```